Automotive lighting company needs professional business card

Hello, we are an automotive lighting company and looking to have a professional business card designed for us. We have included some images which can be used on the card. Website is www.brightarcmotoring.com which has all of our details on it. Email is brightarcmotoring@kelvomail.com phone number is 1300 628 317 thank you guys!

Target Market(s)

Automotive industry

Contact Information for Business Card

Phone - 1300 628 317
Web - www.brightarcmotoring.com
Email - brightarcmotoring@kelvomail.com

Requirements
Must have
• Looking to have a dark theme. Elegant and professional. Needs to look and feel like a high quality card to represent high quality company.

```html
<!DOCTYPE html>
<html lang="en">
<head>
<meta charset="utf-8">
<title>Bright Arc Motoring – Business Card</title>
<link href="https://fonts.googleapis.com/css2?family=Roboto:wght@400;500;700;900&display=swap" rel="stylesheet">
<style>
  :root {
    --stage: #2a2b2d;
    --brand-blue: #0891d1;
    --card-dark: #1f2022;
    --card-dark-edge: #18191b;
    --ink-light: #ffffff;
    --ink-soft: #e6e8ea;
    --rule: #9a9c9f;
  }
  * { margin: 0; padding: 0; box-sizing: border-box; }
  html, body {
    width: 1200px; height: 874px; overflow: hidden;
    background: var(--stage);
    font-family: "Roboto", Arial, sans-serif;
  }
  .stage {
    width: 1200px; height: 874px;
    display: flex; flex-direction: column; align-items: center; justify-content: center;
    gap: 40px;
  }
  .card {
    width: 600px; height: 367px; position: relative; overflow: hidden;
    box-shadow: 0 10px 30px rgba(0,0,0,.45);
  }
  /* Front */
  .card-front { background: var(--brand-blue); }
  .front-name {
    position: absolute; left: 0; right: 0; top: 132px;
    text-align: center; color: var(--ink-light);
    font-weight: 900; font-size: 46px; letter-spacing: 1px;
  }
  .front-url {
    position: absolute; left: 0; right: 0; top: 300px;
    text-align: center; color: var(--ink-light);
    font-size: 15px; letter-spacing: 3.5px;
  }
  /* Back */
  .card-back {
    background: radial-gradient(ellipse at 60% 45%, #26272a 0%, var(--card-dark) 60%, var(--card-dark-edge) 100%);
  }
  .brand-name {
    position: absolute; right: 44px; top: 78px; width: 300px;
    color: var(--ink-light); font-weight: 700; font-size: 30px; line-height: 1.1;
    text-align: right; display: flex; align-items: center; justify-content: flex-end; gap: 12px;
  }
  .brand-dot { width: 14px; height: 14px; border-radius: 50%; background: var(--brand-blue); flex: none; }
  .person { position: absolute; left: 44px; top: 150px; }
  .person-name { color: var(--brand-blue); font-weight: 500; font-size: 27px; }
  .person-role { color: var(--ink-light); font-weight: 500; font-size: 16px; margin-top: 2px; }
  .rule {
    position: absolute; left: 44px; right: 44px; top: 232px;
    height: 1px; background: var(--rule);
  }
  .contacts { position: absolute; left: 44px; top: 198px; list-style: none; display: none; }
  .contact-list { position: absolute; left: 44px; top: 246px; list-style: none; }
  .contact-list li {
    display: flex; align-items: center; gap: 10px;
    color: var(--ink-soft); font-size: 16px; margin-bottom: 8px;
  }
  .contact-list svg { width: 15px; height: 15px; flex: none; fill: var(--brand-blue); }
  .back-url {
    position: absolute; right: 44px; bottom: 30px;
    color: var(--ink-soft); font-size: 16px;
  }
</style>
</head>
<body>
<main class="stage">
  <section class="card card-front">
    <div class="front-name">Bright Arc Motoring</div>
    <div class="front-url">www.brightarcmotoring.com</div>
  </section>

  <section class="card card-back">
    <div class="brand-name"><span class="brand-dot"></span><span>Bright Arc Motoring</span></div>
    <div class="person">
      <div class="person-name">Daniel Harper</div>
      <div class="person-role">President</div>
    </div>
    <div class="rule"></div>
    <ul class="contact-list">
      <li>
        <svg viewBox="0 0 24 24" aria-hidden="true"><path d="M6.6 10.8a15.1 15.1 0 0 0 6.6 6.6l2.2-2.2a1 1 0 0 1 1-.25 11.4 11.4 0 0 0 3.6.57 1 1 0 0 1 1 1V20a1 1 0 0 1-1 1A17 17 0 0 1 3 4a1 1 0 0 1 1-1h3.5a1 1 0 0 1 1 1c0 1.25.2 2.45.57 3.57a1 1 0 0 1-.25 1z"/></svg>
        <span>1300 628 317</span>
      </li>
      <li>
        <svg viewBox="0 0 24 24" aria-hidden="true"><path d="M2 5h20v14H2z" fill="none"/><path d="M2 5h20v2l-10 6L2 7zM2 9l10 6 10-6v10H2z"/></svg>
        <span>brightarcmotoring@kelvomail.com</span>
      </li>
    </ul>
    <div class="back-url">brightarcmotoring.com</div>
  </section>
</main>
</body>
</html>
```